Re-design a training handout - Pathway Keystone

We need a graphic design for a training workbook for leaders to use in a workshop and as a journal.
It is two A3 double sided with fold lines and content already laid out. It is dull & does not capture imagination.

We want it to be something a leader gets as part of a program and cannot not wait to begin filing out the blank sections.
We are calling it a leader "blue print".
It needs to be in Adobe Indesign5 (so we can improve it ourselves over the coming months.
We will send the Indesign file with everything already done EXCEPT the magic of a great layout.
A sample of ONE page (of Four) has been attached. It is page with the most writing.

Reason: I have provided a guarantee to pay and answered some questions which will help. A couple of designers requested extra information and guidance. Thanks again - there will be no further extension. Kind regards. Tom

Target Market(s)

Leaders and executives of team from 10 to 500

Industry/Entity Type

Graphic Design

Requirements
Must have
• Indesign5
work within the A3 with the fold lines already indicated
Be able to written on in the blank or line sections.
Keep the same text.

```html
<!DOCTYPE html>
<html lang="en">
<head>
<meta charset="utf-8">
<title>Leader Blueprint – Workbook Page</title>
<link rel="stylesheet" href="https://fonts.googleapis.com/css2?family=Alegreya+Sans:wght@700;800&display=swap">
<style>
  :root {
    --blueprint: #164a86;
    --blueprint-deep: #0f3666;
    --grid-fine: #2a5d98;
    --grid-major: #3a6fab;
    --chalk: #ffffff;
    --paper: #f4f8fd;
    --ink-blue: #1b4f8e;
    --rule-blue: #8fb2d8;
    --cell-line: #6f98c6;
    --fold: #9fc2e8;
    --accent: #7fd3ff;
  }
  html, body {
    margin: 0;
    padding: 0;
    width: 1200px;
    height: 851px;
    overflow: hidden;
    background: var(--blueprint);
  }
  .sheet {
    display: block;
    width: 1200px;
    height: 851px;
    font-family: "Alegreya Sans", "Trebuchet MS", sans-serif;
  }
  .sheet-ground { fill: url(#blueprint-ground); }
  .grid-fine { fill: none; stroke: var(--grid-fine); stroke-width: 0.6; }
  .grid-major { fill: none; stroke: var(--grid-major); stroke-width: 1; }
  .fold-line { stroke: var(--fold); stroke-width: 1.2; stroke-dasharray: 7 5; opacity: 0.8; }
  .title-block { fill: var(--chalk); }
  .title-accent { fill: var(--accent); }
  .section-title { fill: var(--chalk); font-weight: 800; }
  .title-rule { stroke: var(--chalk); stroke-width: 1.4; }
  .write-line { stroke: var(--rule-blue); stroke-width: 1.3; }
  .frame { fill: var(--paper); stroke: var(--chalk); stroke-width: 4; }
  .frame-corner { fill: none; stroke: var(--accent); stroke-width: 3; }
  .cell-line { stroke: var(--cell-line); stroke-width: 3; }
  .column-head { fill: var(--chalk); }
  .column-label { fill: var(--ink-blue); font-size: 15px; font-weight: 800; }
  .column-divider { stroke: var(--ink-blue); stroke-width: 1.5; }
</style>
</head>
<body>
<svg class="sheet" viewBox="0 0 1200 851" xmlns="http://www.w3.org/2000/svg">
  <defs>
    <radialGradient id="blueprint-ground" cx="50%" cy="40%" r="75%">
      <stop offset="0" stop-color="#1a5597"/>
      <stop offset="1" stop-color="#0f3666"/>
    </radialGradient>
    <pattern id="grid-small" width="12" height="12" patternUnits="userSpaceOnUse">
      <path class="grid-fine" d="M12 0H0V12"/>
    </pattern>
    <pattern id="grid-large" width="60" height="60" patternUnits="userSpaceOnUse">
      <rect width="60" height="60" fill="url(#grid-small)"/>
      <path class="grid-major" d="M60 0H0V60"/>
    </pattern>
  </defs>

  <rect class="sheet-ground" width="1200" height="851"/>
  <rect width="1200" height="851" fill="url(#grid-large)" opacity="0.7"/>

  <g class="folds">
    <line class="fold-line" x1="296" y1="0" x2="296" y2="851"/>
    <line class="fold-line" x1="596" y1="0" x2="596" y2="851"/>
    <line class="fold-line" x1="0" y1="218" x2="1200" y2="218"/>
    <line class="fold-line" x1="0" y1="432" x2="1200" y2="432"/>
    <line class="fold-line" x1="0" y1="634" x2="1200" y2="634"/>
  </g>

  <g class="self-awareness">
    <rect class="title-block" x="0" y="8" width="31" height="51"/>
    <rect class="title-accent" x="0" y="8" width="31" height="6"/>
    <text class="section-title" x="35" y="31" font-size="27" textLength="243" lengthAdjust="spacingAndGlyphs">SELF - AWARENESS</text>
    <text class="section-title" x="35" y="56" font-size="27" textLength="75" lengthAdjust="spacingAndGlyphs">TOOL</text>
    <line class="title-rule" x1="118" y1="53" x2="273" y2="53"/>

    <rect class="title-block" x="0" y="228" width="31" height="51"/>
    <rect class="title-accent" x="0" y="228" width="31" height="6"/>
    <text class="section-title" x="35" y="252" font-size="27" textLength="243" lengthAdjust="spacingAndGlyphs">SELF - AWARENESS</text>
    <text class="section-title" x="35" y="277" font-size="27" textLength="75" lengthAdjust="spacingAndGlyphs">TOOL</text>
    <line class="title-rule" x1="118" y1="275" x2="273" y2="275"/>
  </g>

  <g class="influential-books">
    <text class="section-title" x="311" y="36" font-size="38" textLength="278" lengthAdjust="spacingAndGlyphs">MY INFLUENTIAL</text>
    <text class="section-title" x="311" y="58" font-size="24" textLength="280" lengthAdjust="spacingAndGlyphs">BOOKS / PUBLICATIONS</text>
    <rect class="frame" x="311" y="77" width="268" height="340"/>
    <path class="frame-corner" d="M303 95V69H329M561 425H587V399"/>
    <line class="write-line" x1="320" y1="106" x2="565" y2="106"/>
    <line class="write-line" x1="320" y1="134" x2="565" y2="134"/>
    <line class="write-line" x1="320" y1="162" x2="565" y2="162"/>
    <line class="write-line" x1="320" y1="190" x2="565" y2="190"/>
    <line class="write-line" x1="320" y1="217" x2="565" y2="217"/>
    <line class="write-line" x1="320" y1="244" x2="565" y2="244"/>
    <line class="write-line" x1="320" y1="272" x2="565" y2="272"/>
    <line class="write-line" x1="320" y1="299" x2="565" y2="299"/>
    <line class="write-line" x1="320" y1="327" x2="565" y2="327"/>
    <line class="write-line" x1="320" y1="355" x2="565" y2="355"/>
    <line class="write-line" x1="320" y1="383" x2="565" y2="383"/>
  </g>

  <g class="issues-approach">
    <text class="section-title" x="616" y="36" font-size="39" textLength="420" lengthAdjust="spacingAndGlyphs">ISSUES BASED APPROACH</text>
    <rect class="title-block" x="1046" y="10" width="154" height="23"/>
    <rect class="title-accent" x="1046" y="10" width="8" height="23"/>

    <rect class="column-head" x="614" y="61" width="565" height="24"/>
    <line class="column-divider" x1="811" y1="61" x2="811" y2="85"/>
    <line class="column-divider" x1="991" y1="61" x2="991" y2="85"/>
    <text class="column-label" x="691" y="78" textLength="66" lengthAdjust="spacingAndGlyphs">MY ISSUE</text>
    <text class="column-label" x="825" y="78" textLength="153" lengthAdjust="spacingAndGlyphs">PLANNED APPROACH</text>
    <text class="column-label" x="1017" y="78" textLength="142" lengthAdjust="spacingAndGlyphs">OUTCOME &amp; LEARN</text>

    <rect class="frame" x="615" y="100" width="563" height="699"/>
    <path class="frame-corner" d="M607 118V92H633M1160 807H1186V781"/>
    <line class="cell-line" x1="617" y1="174" x2="1176" y2="174"/>
    <line class="cell-line" x1="617" y1="261" x2="1176" y2="261"/>
    <line class="cell-line" x1="617" y1="348" x2="1176" y2="348"/>
    <line class="cell-line" x1="617" y1="436" x2="1176" y2="436"/>
    <line class="cell-line" x1="617" y1="523" x2="1176" y2="523"/>
    <line class="cell-line" x1="617" y1="611" x2="1176" y2="611"/>
    <line class="cell-line" x1="617" y1="698" x2="1176" y2="698"/>
    <line class="cell-line" x1="811" y1="102" x2="811" y2="797"/>
    <line class="cell-line" x1="991" y1="102" x2="991" y2="797"/>
  </g>
</svg>
</body>
</html>
```